Real Estate agent needs flyer/folder to contain bio and overview of services

I'm including files of the layout of the small folder. The folder is 6 1/2 across and 9 1/2 inches long. It will have a front & back cover and then writing on the 2 inside pages.

I am sending a few files to incorporate into the flyer, 1 new logo to use and 2 files which are coloring ideas.

```html
<!DOCTYPE html>
<html lang="en">
<head>
<meta charset="utf-8">
<title>Clara Vantressi – Realtor Folder</title>
<link href="https://fonts.googleapis.com/css2?family=Libre+Baskerville:ital,wght@0,400;0,700;1,400&family=PT+Sans:wght@400;700&display=swap" rel="stylesheet">
<style>
:root{
  --navy:#27458e;
  --blue:#2f55aa;
  --light:#3d66bf;
  --paper:#f5f5f5;
  --ink:#2e2e2e;
  --muted:#9fb2dd;
  --bg:#e6e6e6;
  --white:#ffffff;
}
*{box-sizing:border-box;margin:0;padding:0}
html,body{width:837px;height:1200px;overflow:hidden;background:var(--bg)}
.canvas{position:relative;width:837px;height:1200px;overflow:hidden;font-family:"PT Sans",sans-serif;color:var(--ink)}
.spread{position:absolute;left:78px;width:680px;height:500px;background:var(--paper);overflow:hidden;box-shadow:0 3px 10px rgba(0,0,0,.25)}
.spread--outer{top:70px}
.spread--inner{top:625px;background:var(--white)}
.shapes{position:absolute;inset:0}
.abs{position:absolute}

/* outer spread */
.back-quote{left:40px;top:352px;width:260px;text-align:center;font-family:"Libre Baskerville",serif;font-style:italic;font-size:10.2px;line-height:1.38;color:var(--white)}
.back-name{left:0;width:340px;top:442px;text-align:center;font-size:10.5px;font-weight:700;letter-spacing:.3px;color:var(--white)}
.contact-row{top:473px;width:340px;display:flex;justify-content:space-around;padding:0 14px;font-size:7.2px;color:var(--white)}
.contact-row span{display:flex;align-items:center;gap:4px}
.icon{width:9px;height:9px;flex:none}
.brand{display:flex;align-items:center;gap:5px;font-family:"PT Sans",sans-serif;font-weight:700;font-size:12px;letter-spacing:1px}
.brand-dot{width:10px;height:10px;border-radius:50%;background:currentColor;display:inline-block}
.brand--back{left:128px;top:286px;color:var(--white)}
.cover-name{left:360px;top:180px;width:300px;text-align:center;font-family:"Libre Baskerville",serif;font-size:26px;line-height:1.1;color:var(--blue);letter-spacing:1px}
.cover-title{left:340px;top:398px;width:340px;text-align:center;font-family:"Libre Baskerville",serif;font-weight:700;font-size:18.5px;line-height:1.4;color:var(--white)}

/* inner spread */
.sidebar{left:0;top:0;width:136px;height:500px;background:var(--navy);color:var(--white)}
.portrait{left:18px;top:22px;width:100px;height:100px;border-radius:50%;border:3px solid var(--light);background:radial-gradient(circle at 50% 40%,#e8d2b6 0%,#c9a57e 55%,#8a8f9c 100%)}
.agent-name{left:0;width:136px;top:140px;text-align:center;font-size:8.5px;color:var(--muted);line-height:1.25}
.agent-name small{display:block;font-size:6px}
.intro-title{left:0;width:136px;top:187px;text-align:center;font-family:"Libre Baskerville",serif;font-size:9.5px}
.intro-text{left:18px;top:206px;width:104px;font-size:6.3px;line-height:1.32;text-align:justify}
.intro-text p{margin-bottom:8px}
.side-name{right:12px;top:431px;font-size:10.5px;font-weight:700;letter-spacing:.3px}
.side-contacts{right:12px;top:450px;font-size:7.2px;line-height:1.9;text-align:right}
.side-contacts div{display:flex;align-items:center;justify-content:flex-end;gap:4px}
.hero{left:136px;top:0;width:544px;height:170px;background:linear-gradient(180deg,#1c2a4a 0%,#3a4e7a 45%,#c89b5e 70%,#2b6fb0 100%)}
.brand--hero{left:583px;top:128px;color:var(--white);font-size:13px}
.col{font-size:6.3px;line-height:1.32;text-align:justify}
.col p{margin-bottom:7px}
.h-sect{font-family:"Libre Baskerville",serif;font-size:10px;color:var(--blue)}
.h-big{font-size:13.5px;color:var(--ink);margin:6px 0 5px}
.testimonial{position:absolute;border:1px solid var(--blue);border-radius:4px;padding:9px 6px 4px;font-family:"Libre Baskerville",serif;font-style:italic;font-size:4.9px;line-height:1.42;color:#555}
.testimonial::before{content:"\201C\201C";position:absolute;top:-9px;left:50%;transform:translateX(-50%);background:var(--white);padding:0 3px;font-size:15px;font-style:normal;font-weight:700;color:var(--blue);line-height:1}
.fold{left:339px;top:170px;width:2px;height:330px;background:linear-gradient(90deg,rgba(0,0,0,.08),rgba(0,0,0,0))}
</style>
</head>
<body>
<div class="canvas">

  <!-- outer spread: back cover + front cover -->
  <section class="spread spread--outer">
    <svg class="shapes" viewBox="0 0 680 500" width="680" height="500">
      <rect x="0" y="0" width="340" height="250" fill="#5b6f93"/>
      <polygon points="0,245 172,143 340,238 340,500 0,500" fill="var(--navy)"/>
      <polygon points="340,238 560,375 680,300 680,500 340,500" fill="var(--navy)"/>
      <polygon points="560,375 680,300 680,430" fill="var(--light)"/>
    </svg>
    <div class="abs" role="img" aria-label="Evening photo of a modern home patio with lounge chairs beside a reflecting pool" style="left:0;top:0;width:340px;height:245px;clip-path:polygon(0 0,100% 0,100% 97%,50.6% 58%,0 100%);background:linear-gradient(160deg,#6b84b4 0%,#3c4a66 45%,#c69a68 70%,#1f2c45 100%)"></div>

    <div class="abs brand brand--back"><span class="brand-dot"></span>CRESTLINE</div>
    <p class="abs back-quote">Along with being your Realtor, I’m a lifelong resource for all things home-related &amp; beyond…if you need a great referral for anything at all, call me! &nbsp;I can’t wait to work with you!</p>
    <p class="abs back-name">CLARA VANTRESSI</p>
    <div class="abs contact-row" style="left:0">
      <span><svg class="icon" viewBox="0 0 10 10"><circle cx="5" cy="5" r="4.3" fill="none" stroke="#fff" stroke-width="1"/><circle cx="5" cy="5" r="1.8" fill="#fff"/></svg>www.claravhomes.com</span>
      <span><svg class="icon" viewBox="0 0 10 10"><circle cx="5" cy="5" r="4.3" fill="none" stroke="#fff" stroke-width="1"/><path d="M3.3 2.8l1 1-.5.7a3 3 0 0 0 1.7 1.7l.7-.5 1 1-.6.8C4.5 7.4 2.6 5.5 2.5 3.4z" fill="#fff"/></svg>555 014 2876</span>
      <span><svg class="icon" viewBox="0 0 10 10"><circle cx="5" cy="5" r="4.3" fill="none" stroke="#fff" stroke-width="1"/><rect x="2.8" y="3.5" width="4.4" height="3" fill="none" stroke="#fff" stroke-width=".7"/><path d="M2.8 3.5L5 5.3 7.2 3.5" fill="none" stroke="#fff" stroke-width=".7"/></svg>clara@claravhomes.com</span>
    </div>

    <p class="abs cover-name">CLARA<br>VANTRESSI</p>
    <p class="abs cover-title">Helping You<br>Make Better Decisions...</p>
    <div class="abs contact-row" style="left:340px">
      <span><svg class="icon" viewBox="0 0 10 10"><circle cx="5" cy="5" r="4.3" fill="none" stroke="#fff" stroke-width="1"/><circle cx="5" cy="5" r="1.8" fill="#fff"/></svg>www.claravhomes.com</span>
      <span><svg class="icon" viewBox="0 0 10 10"><circle cx="5" cy="5" r="4.3" fill="none" stroke="#fff" stroke-width="1"/><path d="M3.3 2.8l1 1-.5.7a3 3 0 0 0 1.7 1.7l.7-.5 1 1-.6.8C4.5 7.4 2.6 5.5 2.5 3.4z" fill="#fff"/></svg>555 014 2876</span>
      <span><svg class="icon" viewBox="0 0 10 10"><circle cx="5" cy="5" r="4.3" fill="none" stroke="#fff" stroke-width="1"/><rect x="2.8" y="3.5" width="4.4" height="3" fill="none" stroke="#fff" stroke-width=".7"/><path d="M2.8 3.5L5 5.3 7.2 3.5" fill="none" stroke="#fff" stroke-width=".7"/></svg>clara@claravhomes.com</span>
    </div>
  </section>

  <!-- inner spread -->
  <section class="spread spread--inner">
    <aside class="abs sidebar">
      <div class="abs portrait" role="img" aria-label="Portrait photo of the realtor"></div>
      <p class="abs agent-name">Clara Vantressi<br>Realtor ®<small>DRE# 01234567</small></p>
      <h2 class="abs intro-title">Let me introduce myself</h2>
      <div class="abs intro-text">
        <p>I’m originally from Chicago, but I’m a full-fledged California girl now. I’ve lived and worked in Orange County since 1996. I always say where we live is the next best thing to living on a tropical island. I’ve traveled to many and I’m always happy to come back to my Laguna Niguel home.</p>
        <p>My passion for this area is why I’m in Real Estate. I consider myself incredibly fortunate to sell homes and help people purchase homes in an area that I love with all my heart.</p>
        <p>This passion also carries over in representing my clients with the highest degree of professionalism, enthusiasm and care. My business is built on exceptional customer service and I’m grateful my clients are mostly repeat and referrals.</p>
      </div>
      <p class="abs side-name">CLARA VANTRESSI</p>
      <div class="abs side-contacts">
        <div>555 014 2876 <svg class="icon" viewBox="0 0 10 10"><circle cx="5" cy="5" r="4.3" fill="none" stroke="#fff" stroke-width="1"/><path d="M3.3 2.8l1 1-.5.7a3 3 0 0 0 1.7 1.7l.7-.5 1 1-.6.8C4.5 7.4 2.6 5.5 2.5 3.4z" fill="#fff"/></svg></div>
        <div>clara@claravhomes.com <svg class="icon" viewBox="0 0 10 10"><circle cx="5" cy="5" r="4.3" fill="none" stroke="#fff" stroke-width="1"/><rect x="2.8" y="3.5" width="4.4" height="3" fill="none" stroke="#fff" stroke-width=".7"/><path d="M2.8 3.5L5 5.3 7.2 3.5" fill="none" stroke="#fff" stroke-width=".7"/></svg></div>
        <div>www.claravhomes.com <svg class="icon" viewBox="0 0 10 10"><circle cx="5" cy="5" r="4.3" fill="none" stroke="#fff" stroke-width="1"/><circle cx="5" cy="5" r="1.8" fill="#fff"/></svg></div>
      </div>
    </aside>

    <div class="abs hero" role="img" aria-label="Night photo of a lit luxury home with a glowing swimming pool in the foreground"></div>
    <div class="abs brand brand--hero">CRESTLINE<span class="brand-dot"></span></div>
    <div class="abs fold"></div>

    <div class="abs col" style="left:146px;top:187px;width:184px">
      <h3 class="h-sect">My Core Tenet</h3>
      <h4 class="h-big">It’s All About YOU!</h4>
      <p>My #1 priority is understanding YOUR needs and YOUR objectives.</p>
      <p>This understanding, along with working diligently on your behalf, means we accomplish your goal whether you’re purchasing your 1st home or selling a home you’ve loved so you can move on to the next chapter of your life.</p>
      <h3 class="h-sect" style="margin:18px 0 8px">Real Estate Services &amp; Beyond...</h3>
      <p>Simply put, I help people who are local, relocating and investing, sell and purchase homes in Southern California. For purchases outside of California, I can refer to a network of agents across the country.</p>
      <p>I also provide a team who is dedicated to providing outstanding customer service throughout the transaction. My team includes a network of lenders, title, and escrow officers, in house CPA, stagers, photographers, contractors and more.</p>
    </div>
    <blockquote class="testimonial" style="left:146px;top:440px;width:184px">Clara got us an amazing deal on our new home and sold our old home in a week. Clara is patient, hardworking, professional and most importantly HONEST. Clara is definitely one of the best in the business!<br>- Nadia &amp; Owen Hale</blockquote>

    <div class="abs col" style="left:352px;top:187px;width:316px">
      <h3 class="h-sect" style="text-align:center;margin-bottom:8px">Selling Your Home</h3>
      <p>Selling your home is not like any other business transaction. It’s also personal. My priority as your Listing Agent is to guide you through what can be a complicated and sometimes emotional process.</p>
      <p>I place great emphasis on marketing your property with professional photographs, along with harnessing the power of the Internet and the virtual world to reach as many buyers as possible. Your property will be marketed to the public as well as to other agents, thus creating maximum exposure of your home.</p>
      <p>When we first meet to discuss selling your home, it’s essential for me to gain an understanding of your unique needs such as timelines, expectations and financial considerations, just to name a few. From there, I begin the process of listing and marketing your home. I lead you through negotiations and more paperwork than you ever care to do, guiding you to the successful closing of your home.</p>
      <h3 class="h-sect" style="text-align:center;margin:12px 0 8px">Buying a Home</h3>
      <p>If you’re thinking about buying a home, it’s imperative you have an accomplished, real estate professional by your side to walk you through what is likely the largest purchase of your life.</p>
      <p>To get started, I like to meet with you so we have an opportunity to get to know each other as purchasing a home is a uniquely personal endeavor. At that time, we can discuss your goals and if it’s a good time for you to purchase a home.</p>
      <p>From there, the first step is to obtain a pre-approval from a lender. I’m able to recommend various lenders who can introduce and explain the various loan products available. After you’ve been pre-approved, that’s when the fun starts! I guide you through the home buying adventure every step of the way and look forward to handing you the keys to your new home.</p>
    </div>
    <blockquote class="testimonial" style="left:368px;top:440px;width:148px">Clara is the kind of Real Estate professional everyone wants to represent them. She is knowledgeable, ethical, energetic, and follows up on every detail. We were lucky to find her!<br>- Victor &amp; Jane Morrow</blockquote>
    <blockquote class="testimonial" style="left:530px;top:440px;width:148px">During the home buying process, Clara becomes your trusted advisor, mentor and friend. Clara is unequivocally the reason why I was able to purchase my home in Laguna Niguel and provide my family with a world-class community.<br>- Teodoro Alvane</blockquote>
  </section>

</div>
</body>
</html>
```